Team email banner for internal communications

We need a team email banner/header that will be applied to all internal communications from our department to other functions. The graphic should be optimized for Outlook and be landscape in layout. We have 5 different silo within our team and will need so will either need have a blank space to denote each team or have change in colors/graphics to denote each team (see current headers attached to job description). We are looking for a banner that combines our team logo (attached) with our team name, Commercial Learning & Development. The theme should be L&D and pharmaceutical in nature.

Need extra days to review

The text in the banner should be Commercial Learning & Development with the team logo (attached).

```html
<!DOCTYPE html>
<html lang="en">
<head>
<meta charset="UTF-8">
<title>Commercial Learning &amp; Development – Team Banner</title>
<link rel="stylesheet" href="https://fonts.googleapis.com/css2?family=Poppins:wght@700&family=Montserrat:wght@600&display=swap">
<style>
  :root {
    --stage: #eef1f3;
    --paper: #ffffff;
    --ink: #0b0b0b;
    --brand-red: #d9291c;
    --magenta: #cf1f6b;
    --cyan: #4fe3ef;
    --violet: #6d4bb0;
    --hot-pink: #e0237a;
    --pink-soft: #f7d3e0;
    --blue-soft: #cdeaf3;
    --lilac-soft: #e3d9ef;
  }
  * { margin: 0; padding: 0; box-sizing: border-box; }
  html, body { width: 1200px; height: 532px; overflow: hidden; background: var(--stage); }
  .banner {
    position: absolute; left: 0; top: 66px;
    width: 1200px; height: 400px;
    background: var(--paper);
    overflow: hidden;
  }
  .wave-field { position: absolute; inset: 0; }
  .team-mark {
    position: absolute; left: 311px; top: 58px;
    width: 141px; text-align: center;
  }
  .team-mark__dot {
    display: block; width: 40px; height: 40px; margin: 0 auto 12px;
    border-radius: 50%; background: var(--brand-red);
  }
  .team-mark__name {
    display: block;
    font-family: "Poppins", sans-serif; font-weight: 700;
    font-size: 28px; line-height: 40px; color: var(--ink);
  }
  .divider {
    position: absolute; left: 465px; top: 70px;
    width: 2px; height: 104px; background: #555;
  }
  .team-name {
    position: absolute; left: 481px; top: 60px;
    font-family: "Poppins", sans-serif; font-weight: 700;
    font-size: 41px; line-height: 40px; color: var(--ink);
    text-transform: uppercase; letter-spacing: -0.4px;
    white-space: nowrap;
  }
  .rule {
    position: absolute; left: 311px; top: 204px;
    width: 459px; height: 2px; background: var(--magenta);
  }
  .silo {
    position: absolute; left: 311px; top: 217px;
    width: 459px; text-align: center;
    font-family: "Montserrat", sans-serif; font-weight: 600;
    font-size: 34.5px; line-height: 34px;
    color: var(--magenta); white-space: nowrap;
  }
  .photo {
    position: absolute; left: 832px; top: 43px;
    width: 308px; height: 308px; border-radius: 50%;
    background: radial-gradient(circle at 40% 55%, #cfe3f1 0%, #8fb7d8 35%, #6f9e7a 70%, #46615a 100%);
  }
  .ring { position: absolute; inset: 0; }
</style>
</head>
<body>
  <section class="banner">
    <svg class="wave-field" width="1200" height="400" viewBox="0 0 1200 400" role="img" aria-label="Decorative flowing line-mesh waves in cyan, violet and magenta">
      <defs>
        <linearGradient id="coolFill" x1="0" y1="0" x2="1" y2="1">
          <stop offset="0" stop-color="#4fe3ef" stop-opacity="0.18"/>
          <stop offset="1" stop-color="#6d4bb0" stop-opacity="0.35"/>
        </linearGradient>
        <linearGradient id="warmFill" x1="0" x2="1">
          <stop offset="0" stop-color="#6d4bb0" stop-opacity="0.35"/>
          <stop offset="1" stop-color="#e0237a" stop-opacity="0.2"/>
        </linearGradient>
        <linearGradient id="pinkBand" x1="0" x2="1">
          <stop offset="0" stop-color="#e0237a" stop-opacity="0.9"/>
          <stop offset="1" stop-color="#e0237a" stop-opacity="0.6"/>
        </linearGradient>
      </defs>
      <path d="M0 177 C200 180 340 240 440 400 L0 400 Z" fill="url(#coolFill)"/>
      <path d="M420 400 C560 360 660 300 760 300 C860 300 940 350 1000 400 Z" fill="url(#warmFill)"/>
      <path d="M815 400 C870 380 910 360 950 340 L975 352 C930 375 890 392 860 400 Z" fill="url(#pinkBand)"/>
      <path d="M1150 195 C1168 190 1184 186 1200 181 L1200 210 C1184 214 1168 220 1152 226 Z" fill="url(#pinkBand)"/>
    </svg>

    <svg class="ring" width="1200" height="400" viewBox="0 0 1200 400" aria-hidden="true">
      <circle cx="855" cy="73" r="18" fill="var(--pink-soft)"/>
      <circle cx="1127" cy="51" r="10" fill="var(--blue-soft)"/>
      <circle cx="1113" cy="330" r="6" fill="var(--lilac-soft)"/>
    </svg>

    <div class="photo" role="img" aria-label="Photo of a gloved hand holding a glass slide with a seedling, overlaid with digital hexagon graphics"></div>

    <svg class="ring" width="1200" height="400" viewBox="0 0 1200 400" aria-hidden="true">
      <defs>
        <linearGradient id="ringStroke" x1="0" y1="0" x2="1" y2="1">
          <stop offset="0" stop-color="#4fe3ef"/>
          <stop offset="0.5" stop-color="#6d4bb0"/>
          <stop offset="1" stop-color="#e0237a"/>
        </linearGradient>
      </defs>
      <circle cx="986" cy="197" r="170" fill="none" stroke="url(#ringStroke)" stroke-width="1.6"/>
    </svg>

    <div class="team-mark">
      <span class="team-mark__dot"></span>
      <span class="team-mark__name">VERIDAN</span>
    </div>
    <div class="divider"></div>
    <h1 class="team-name">Commercial<br>Learning &amp;<br>Development</h1>
    <div class="rule"></div>
    <p class="silo">Operational &amp; Capabilities</p>
  </section>
</body>
</html>
```